Business card for a gourmet fruit and vegetable retail store

Please design a business card for our boutique gourmet fruit and vegetable food store using attached logo design, with the colour options of white, black and lime green. We would like it to be unique and classic, with a large image of the logo on the back of the business card, and the business card details plus a design on the front.

Target Market(s)

High income earners in an affluent Melbourne suburb who value high quality products and done mind paying for it

Industry/Entity Type

Retail

Contact Information for Business Card

Business name: Harwick's Fine Food Merchant
Address: 27 Plumtree Rd, Kelsby VIC 3158
Name: TBC
Position Title: Director
Phone Number: TBC
Mobile: TBC

Business name is: Harwick's Fine Food Merchant. Please allow space for us to fill in the business address, contact number, person's name, position Title and mobile number.

Colors
acd036

Requirements
Must have
• The logo must have our business logo on the back, and our business details and contact details on the front. It must include the colours of white, black and lime green
Nice to have
• It can have different background colours on the front and on the back.
Should not have
• It should not have any other colours aside from white, black and lime green

```html
<!DOCTYPE html>
<html lang="en">
<head>
<meta charset="utf-8">
<title>Harwick's Fine Food Merchant – Business Card</title>
<link href="https://fonts.googleapis.com/css2?family=Libre+Baskerville:wght@400;700&display=swap" rel="stylesheet">
<style>
  :root {
    --lime: #acd036;
    --lime-deep: #8fbf1f;
    --lime-soft: #b9dc6e;
    --lime-pale: #dcefa8;
    --ink: #1c1c1c;
    --black: #000000;
    --backdrop: #f2f2f2;
  }
  * { margin: 0; padding: 0; box-sizing: border-box; }
  html, body {
    width: 1200px;
    height: 1200px;
    overflow: hidden;
    background: var(--backdrop);
  }
  .canvas {
    position: relative;
    width: 1200px;
    height: 1200px;
  }
  .card {
    position: absolute;
    left: 225px;
    width: 750px;
    height: 426px;
    overflow: hidden;
  }
  .card--front { top: 93px; background: var(--ink); }
  .card--back  { top: 610px; background: var(--lime); }

  .front-accent {
    position: absolute;
    left: 0; top: 0;
    width: 200px; height: 426px;
  }
  .identity {
    position: absolute;
    right: 48px;
    top: 76px;
    text-align: right;
    color: var(--lime);
    font-family: "Libre Baskerville", Georgia, serif;
    font-weight: 700;
    text-transform: uppercase;
  }
  .identity__name { font-size: 33px; line-height: 1.1; }
  .identity__role { font-size: 21px; margin-top: 6px; }

  .contacts {
    position: absolute;
    left: 176px;
    top: 215px;
    list-style: none;
    color: var(--lime);
    font-family: "Libre Baskerville", Georgia, serif;
    font-weight: 700;
    font-size: 20px;
    text-transform: uppercase;
  }
  .contacts__item {
    display: flex;
    align-items: center;
    height: 42px;
  }
  .contacts__icon {
    width: 24px; height: 24px;
    margin-right: 26px;
    fill: var(--lime-soft);
    flex: none;
  }

  .brand-mark {
    position: absolute;
    left: 233px;
    top: 72px;
    width: 284px;
    height: 284px;
    border: 3px solid var(--black);
    border-radius: 50%;
    display: flex;
    align-items: center;
    justify-content: center;
  }
  .brand-mark__name {
    font-family: "Libre Baskerville", Georgia, serif;
    font-weight: 700;
    font-size: 34px;
    letter-spacing: 3px;
    color: var(--black);
    text-transform: uppercase;
  }
</style>
</head>
<body>
<main class="canvas">
  <section class="card card--front" aria-label="Business card front">
    <svg class="front-accent" viewBox="0 0 200 426" aria-hidden="true">
      <polygon points="0,0 177,75 0,426" fill="var(--lime-deep)"/>
      <polygon points="0,0 160,58 0,410" fill="var(--lime)"/>
      <polygon points="14,34 140,80 14,390" fill="var(--lime-soft)" stroke="var(--lime-pale)" stroke-width="7"/>
    </svg>

    <div class="identity">
      <p class="identity__name">Name: TBC</p>
      <p class="identity__role">Director</p>
    </div>

    <ul class="contacts">
      <li class="contacts__item">
        <svg class="contacts__icon" viewBox="0 0 24 24" aria-hidden="true"><path d="M6.6 3.5l2.6 3.6c.4.5.3 1.2-.1 1.6L7.6 10.2c1 2.3 3.9 5.3 6.2 6.2l1.5-1.5c.4-.4 1.1-.5 1.6-.1l3.6 2.6c.5.4.6 1.1.2 1.6l-1.6 2.2c-.6.8-1.7 1.1-2.6.7C9.6 19.4 4.6 14.4 2.1 7.5c-.3-.9 0-2 .8-2.6L5 3.3c.5-.4 1.2-.3 1.6.2z"/></svg>
        <span>Phone Number: TBC</span>
      </li>
      <li class="contacts__item">
        <svg class="contacts__icon" viewBox="0 0 24 24" aria-hidden="true"><path d="M8 1.5h8a2 2 0 0 1 2 2v17a2 2 0 0 1-2 2H8a2 2 0 0 1-2-2v-17a2 2 0 0 1 2-2zm0 3v13h8v-13z"/></svg>
        <span>Mobile: TBC</span>
      </li>
      <li class="contacts__item">
        <svg class="contacts__icon" viewBox="0 0 24 24" aria-hidden="true"><path d="M12 1.5a7 7 0 0 1 7 7c0 5-7 14-7 14s-7-9-7-14a7 7 0 0 1 7-7zm0 4.2a2.8 2.8 0 1 0 0 5.6 2.8 2.8 0 0 0 0-5.6z"/></svg>
        <span>27 Plumtree Rd, Kelsby VIC 3158</span>
      </li>
      <li class="contacts__item">
        <svg class="contacts__icon" viewBox="0 0 24 24" aria-hidden="true"><path d="M9 3h6a1.5 1.5 0 0 1 1.5 1.5V6H21a1.5 1.5 0 0 1 1.5 1.5v12A1.5 1.5 0 0 1 21 21H3a1.5 1.5 0 0 1-1.5-1.5v-12A1.5 1.5 0 0 1 3 6h4.5V4.5A1.5 1.5 0 0 1 9 3zm0 1.5V6h6V4.5z"/></svg>
        <span>Harwick's Fine Food Merchant</span>
      </li>
    </ul>
  </section>

  <section class="card card--back" aria-label="Business card back">
    <div class="brand-mark">
      <p class="brand-mark__name">Harwick's</p>
    </div>
  </section>
</main>
</body>
</html>
```